Create Business cards for Pet business

Original Business card creation
Please be original. If I wanted a generic business card template, I would have made one myself
Please use colour scheme

Adobe Files like PSD and AI are required
Name : Kevin Tash
Website : [login to view URL]
Phone number :0491736258

```html
<!DOCTYPE html>
<html lang="en">
<head>
<meta charset="utf-8">
<title>Pawnook Business Cards</title>
<link href="https://fonts.googleapis.com/css2?family=Lato:wght@400;700;900&display=swap" rel="stylesheet">
<style>
  :root {
    --backdrop: #2d2d2d;
    --card: #ffffff;
    --orange: #f39a1f;
    --blue: #1f6db6;
    --grey: #6d6d6d;
    --ink: #555555;
  }
  * { margin: 0; padding: 0; box-sizing: border-box; }
  html, body { width: 1200px; height: 1200px; overflow: hidden; }
  body {
    background: var(--backdrop);
    font-family: 'Lato', sans-serif;
    position: relative;
  }
  .card {
    position: absolute;
    width: 700px;
    height: 406px;
    background: var(--card);
    border-radius: 22px;
    overflow: hidden;
  }
  .card--front { left: 262px; top: 187px; }
  .card--back { left: 257px; top: 641px; }

  .brand-disc {
    position: absolute;
    width: 300px;
    height: 300px;
    border-radius: 50%;
    background: var(--orange);
  }
  .card--front .brand-disc { left: 40px; top: 53px; }
  .card--back .brand-disc { right: 40px; top: 53px; }

  .brand-name {
    position: absolute;
    font-weight: 900;
    color: var(--blue);
    letter-spacing: 0.5px;
    line-height: 1;
  }
  .card--front .brand-name { left: 365px; top: 245px; font-size: 72px; }
  .card--back .brand-name { left: 40px; top: 45px; font-size: 64px; }

  .holder { position: absolute; left: 52px; top: 200px; }
  .holder__name { font-size: 34px; font-weight: 700; color: var(--blue); line-height: 1.1; }
  .holder__name .surname { color: var(--orange); }
  .holder__role { font-size: 17px; color: var(--grey); margin-top: 2px; }

  .contacts { position: absolute; left: 52px; top: 280px; list-style: none; }
  .contacts li {
    display: flex;
    align-items: center;
    gap: 10px;
    font-size: 18px;
    color: var(--ink);
    height: 30.5px;
  }
  .contacts svg { width: 22px; height: 22px; flex: none; }
</style>
</head>
<body>
  <section class="card card--front">
    <div class="brand-disc"></div>
    <div class="brand-name">Pawnook</div>
  </section>

  <section class="card card--back">
    <div class="brand-name">Pawnook</div>
    <div class="holder">
      <div class="holder__name">Kevin <span class="surname">Tash</span></div>
      <div class="holder__role">General Manager</div>
    </div>
    <ul class="contacts">
      <li>
        <svg viewBox="0 0 22 22"><circle cx="11" cy="11" r="11" fill="#f39a1f"/><path d="M7.5 6.5c.6-.6 1.4-.5 1.8.1l1 1.5c.3.5.2 1.1-.2 1.5l-.6.5c.6 1.3 1.5 2.2 2.8 2.8l.5-.6c.4-.4 1-.5 1.5-.2l1.5 1c.6.4.7 1.2.1 1.8l-.8.8c-3.7.4-8-3.9-7.6-7.6z" fill="#fff"/></svg>
        0491736258
      </li>
      <li>
        <svg viewBox="0 0 22 22"><circle cx="11" cy="11" r="11" fill="#1f6db6"/><rect x="5.5" y="7" width="11" height="8" rx="1" fill="#fff"/><path d="M5.8 7.4 11 11.5l5.2-4.1" fill="none" stroke="#1f6db6" stroke-width="1.2"/></svg>
        info@kevintash.com
      </li>
      <li>
        <svg viewBox="0 0 22 22"><circle cx="11" cy="11" r="11" fill="#f39a1f"/><circle cx="11" cy="11" r="5.5" fill="none" stroke="#fff" stroke-width="1.4"/><path d="M5.5 11h11M11 5.5c-2.4 3-2.4 8 0 11M11 5.5c2.4 3 2.4 8 0 11" fill="none" stroke="#fff" stroke-width="1.2"/></svg>
        www.kevintash.com
      </li>
    </ul>
    <div class="brand-disc"></div>
  </section>
</body>
</html>
```